Postcard Design

A house cleaning business. Focus on time saving and stress free. Free estimates. Want it to state that we can make your home sparkle or shine. I have been using the colors purple and black in the logo which I will attach.

Reason: I need a few more days to decide on this. Thank you

Industry/Entity Type

House

Colors
886aae
6b449b

Requirements
Must have
• website www.tidwellhavenhomes.us
phone # 555-390-6172

```html
<!DOCTYPE html>
<html lang="en">
<head>
<meta charset="utf-8">
<title>Tidwell Haven Cleaning Company – Postcard</title>
<link rel="stylesheet" href="https://fonts.googleapis.com/css2?family=Lato:wght@400;700;900&family=Great+Vibes&display=swap">
<style>
  :root {
    --purple: #886aae;
    --purple-deep: #6b449b;
    --sky: #8cc6ec;
    --sky-pale: #d8ecf9;
    --ink: #231f24;
    --white: #ffffff;
    --page: #e6e6e8;
    --line: #333333;
  }
  * { box-sizing: border-box; margin: 0; padding: 0; }
  html, body { width: 900px; height: 1200px; overflow: hidden; }
  body { background: var(--page); position: relative; font-family: "Lato", sans-serif; }

  .card {
    position: absolute; left: 117px; width: 670px; height: 518px;
    background: var(--white); overflow: hidden;
    box-shadow: 0 4px 14px rgba(0,0,0,.18);
  }
  .card--front { top: 57px; }
  .card--back { top: 637px; }
  .card__art { position: absolute; inset: 0; width: 100%; height: 100%; }

  /* Front */
  .front__url { position: absolute; left: 25px; top: 17px; font-size: 18px; color: var(--ink); }
  .front__tagline {
    position: absolute; left: 40px; top: 360px; font-family: "Great Vibes", cursive;
    font-weight: 400; line-height: 1; text-shadow: 2px 2px 3px rgba(0,0,0,.35);
  }
  .front__tagline-top { display: block; font-size: 54px; color: var(--white); }
  .front__tagline-bottom { display: block; font-size: 44px; color: var(--ink); margin-top: 8px; margin-left: 4px; text-shadow: none; }
  .brand {
    position: absolute; left: 420px; top: 320px; width: 230px;
    display: flex; align-items: center; gap: 10px;
  }
  .brand__mark { width: 26px; height: 26px; flex: none; background: var(--ink); border-radius: 50%; }
  .brand__name { font-size: 24px; font-weight: 700; color: var(--ink); line-height: 1.1; }

  /* Back */
  .pill {
    position: absolute; left: 0; width: 198px; height: 54px; padding-left: 27px;
    background: var(--sky); border-radius: 0 27px 27px 0;
    box-shadow: 2px 3px 5px rgba(0,0,0,.25);
    color: var(--white); font-size: 27px; font-weight: 900; line-height: 54px;
  }
  .pill--about { top: 51px; }
  .pill--services { top: 248px; width: 200px; }
  .about__text {
    position: absolute; left: 26px; top: 124px; width: 262px;
    color: var(--white); font-size: 15px; line-height: 20px;
  }
  .services__list { position: absolute; left: 44px; top: 312px; list-style: none; color: var(--white); font-size: 21px; line-height: 28px; }
  .services__list li::before {
    content: ""; display: inline-block; width: 7px; height: 7px; border-radius: 50%;
    background: var(--sky); margin-right: 11px; vertical-align: middle; position: relative; top: -2px;
  }
  .portrait {
    position: absolute; left: 276px; top: 155px; width: 150px; height: 150px;
    border-radius: 50%; border: 4px solid var(--purple);
    background: radial-gradient(circle at 50% 55%, #3a4360 0 18%, #f4f4f6 40%, #ffffff 70%);
  }
  .stamp { position: absolute; left: 553px; top: 114px; width: 64px; height: 67px; border: 1px solid var(--line); }
  .address-line { position: absolute; left: 433px; width: 183px; border-top: 1px solid var(--line); }
  .address-line:nth-of-type(1) { top: 253px; }
  .address-line:nth-of-type(2) { top: 284px; }
  .address-line:nth-of-type(3) { top: 316px; }
  .call { position: absolute; left: 43px; top: 460px; font-size: 21px; color: var(--ink); }
  .call__label { font-weight: 900; }
</style>
</head>
<body>

<section class="card card--front" aria-label="Postcard front">
  <svg class="card__art" viewBox="0 0 670 518" preserveAspectRatio="none" aria-hidden="true">
    <defs>
      <linearGradient id="photoTone" x1="0" y1="0" x2="1" y2="1">
        <stop offset="0" stop-color="#f3e4b8"/>
        <stop offset=".45" stop-color="#e9c86c"/>
        <stop offset="1" stop-color="#d9526a"/>
      </linearGradient>
      <linearGradient id="frontSky" x1="0" y1="0" x2="1" y2="0">
        <stop offset="0" stop-color="#8cc6ec"/>
        <stop offset=".6" stop-color="#e6f3fb"/>
        <stop offset="1" stop-color="#ffffff"/>
      </linearGradient>
    </defs>
    <rect x="150" y="0" width="520" height="260" fill="url(#photoTone)" opacity=".55" role="img" aria-label="Photo of a gloved hand scrubbing with a soapy sponge"/>
    <path d="M0,218 C120,250 250,258 380,238 C470,224 560,210 670,215 V260 H0 Z" fill="url(#frontSky)"/>
    <path d="M0,300 C140,318 290,300 400,262 C500,228 590,212 670,222 V518 H0 Z" fill="var(--purple)"/>
  </svg>
  <p class="front__url">www.tidwellhavenhomes.us</p>
  <h1 class="front__tagline">
    <span class="front__tagline-top">We can make</span>
    <span class="front__tagline-bottom">your home sparkle</span>
  </h1>
  <div class="brand">
    <span class="brand__mark"></span>
    <span class="brand__name">Tidwell Haven Cleaning Company</span>
  </div>
</section>

<section class="card card--back" aria-label="Postcard back">
  <svg class="card__art" viewBox="0 0 670 518" preserveAspectRatio="none" aria-hidden="true">
    <defs>
      <linearGradient id="backSky" x1="0" y1="0" x2="1" y2="1">
        <stop offset="0" stop-color="#8cc6ec"/>
        <stop offset="1" stop-color="#e6f3fb"/>
      </linearGradient>
      <linearGradient id="baseSky" x1="0" y1="0" x2="1" y2="0">
        <stop offset="0" stop-color="#8cc6ec"/>
        <stop offset=".5" stop-color="#ffffff"/>
      </linearGradient>
    </defs>
    <path d="M290,0 H330 C345,70 330,130 345,200 C365,290 420,360 395,450 C380,490 330,510 300,518 H260 C320,480 360,430 350,360 C340,290 300,230 310,150 C315,90 310,40 290,0 Z" fill="url(#backSky)"/>
    <path d="M0,0 H292 C312,40 318,90 312,150 C302,230 340,290 352,360 C362,420 330,445 300,440 C200,430 100,420 0,430 Z" fill="var(--purple)"/>
    <path d="M0,430 C110,420 220,430 300,440 C330,445 340,470 300,518 H0 Z" fill="url(#baseSky)" opacity=".85"/>
  </svg>

  <h2 class="pill pill--about">ABOUT US</h2>
  <p class="about__text">A house cleaning business. Focus on time saving and stress free. Free estimates. Want it to state that we can make your home sparkle or shine.</p>

  <h2 class="pill pill--services">SERVICES</h2>
  <ul class="services__list">
    <li>Cleaning</li>
    <li>Time saving</li>
    <li>Stress free</li>
  </ul>

  <div class="portrait" role="img" aria-label="Photo of a cleaner in navy overalls holding a mop"></div>

  <div class="stamp" aria-label="Stamp area"></div>
  <div class="address-line"></div>
  <div class="address-line"></div>
  <div class="address-line"></div>

  <p class="call"><span class="call__label">Call us :</span> 555-390-6172</p>
</section>

</body>
</html>
```